Creative Businesss Card desgin!

Create a business card for our business Gleam window cleaning!
We are open to creative ideas as long as it maintains a professional image.

Target Market(s)

Small Commercial window cleaning clients including car dealerships, strata manager, cafe

Industry/Entity Type

Window Cleaning

Contact Information for Business Card

Daniel Prescott
General Manager
Gleam Window Cleaning

daniel@gleamservices.com.au
pane-care-southbank.com.au
Ph: 1800 GET GLEAM
Mob: 0437 582 061

Colors
fbed22
0392cd

Requirements
Should not have
• Stock window cleaning/ squeegee graphics

```html
<!DOCTYPE html>
<html lang="en">
<head>
<meta charset="utf-8">
<title>Gleam Window Cleaning — Business Card</title>
<link rel="stylesheet" href="https://fonts.googleapis.com/css2?family=Lato:wght@400;700;900&display=swap">
<style>
  :root {
    --stage: #2a2a2a;
    --card-blue: #04568a;
    --brand-yellow: #fbed22;
    --text-white: #ffffff;
  }
  * { margin: 0; padding: 0; box-sizing: border-box; }
  html, body {
    width: 1200px; height: 960px; overflow: hidden;
    background: var(--stage);
    font-family: "Lato", Arial, sans-serif;
  }
  .canvas { position: relative; width: 1200px; height: 960px; }
  .card {
    position: absolute; left: 280px; width: 655px; height: 373px;
    background: var(--card-blue);
    box-shadow: 0 4px 14px rgba(0,0,0,0.45);
  }
  .card--front { top: 80px; }
  .card--back { top: 506px; }

  .brand { position: absolute; color: var(--brand-yellow); font-weight: 900; line-height: 1; }
  .brand__name { display: block; letter-spacing: 1px; }
  .brand__tagline { display: block; letter-spacing: 0.3px; }

  .card--front .brand { left: 60px; top: 60px; }
  .card--front .brand__name { font-size: 47px; }
  .card--front .brand__tagline { font-size: 17px; margin-top: 6px; }

  .holder { position: absolute; left: 60px; top: 176px; }
  .holder__name { color: var(--brand-yellow); font-size: 26px; font-weight: 700; line-height: 1.1; }
  .holder__title { color: var(--text-white); font-size: 16px; margin-top: 6px; }

  .contact-list { position: absolute; left: 60px; top: 243px; list-style: none; }
  .contact-list li {
    display: flex; align-items: center; height: 22px;
    color: var(--text-white); font-size: 15.5px;
  }
  .contact-list svg { width: 14px; height: 14px; margin-right: 10px; fill: var(--brand-yellow); flex: none; }

  .card--back .brand { left: 0; right: 0; top: 142px; text-align: center; }
  .card--back .brand__name { font-size: 80px; }
  .card--back .brand__tagline { font-size: 24px; margin-top: 10px; }
  .card--back .site {
    position: absolute; left: 0; right: 0; top: 305px; text-align: center;
    color: var(--text-white); font-size: 15px;
  }
</style>
</head>
<body>
<main class="canvas">
  <section class="card card--front">
    <div class="brand">
      <span class="brand__name">GLEAM</span>
      <span class="brand__tagline">WINDOW CLEANING</span>
    </div>
    <div class="holder">
      <p class="holder__name">Daniel Prescott</p>
      <p class="holder__title">General Manager</p>
    </div>
    <ul class="contact-list">
      <li>
        <svg viewBox="0 0 16 16" aria-hidden="true"><path d="M4 1l3 3-2 2c1 2 3 4 5 5l2-2 3 3-2 3C7 15 1 9 1 3z"/></svg>
        1800 GET GLEAM
      </li>
      <li>
        <svg viewBox="0 0 16 16" aria-hidden="true"><path d="M4 0h8a1 1 0 011 1v14a1 1 0 01-1 1H4a1 1 0 01-1-1V1a1 1 0 011-1zm1 2v10h6V2zm3 11a1 1 0 100 2 1 1 0 000-2z"/></svg>
        0437 582 061
      </li>
      <li>
        <svg viewBox="0 0 16 16" aria-hidden="true"><path d="M0 3h16v10H0zm1 1l7 5 7-5v-0H1z"/></svg>
        daniel@gleamservices.com.au
      </li>
      <li>
        <svg viewBox="0 0 16 16" aria-hidden="true"><path d="M8 0a8 8 0 100 16A8 8 0 008 0zm0 1.5c.8 0 1.8 1.8 2.1 5H5.9C6.2 3.3 7.2 1.5 8 1.5zM1.6 7.5h3c0-2 .4-3.7 1-4.9A6.5 6.5 0 001.6 7.5zm12.8 0a6.5 6.5 0 00-4-4.9c.6 1.2 1 2.9 1 4.9zM5.9 8.5h4.2c-.3 3.2-1.3 5-2.1 5s-1.8-1.8-2.1-5zm-4.3 0a6.5 6.5 0 004 4.9c-.6-1.2-1-2.9-1-4.9zm12.8 0h-3c0 2-.4 3.7-1 4.9a6.5 6.5 0 004-4.9z"/></svg>
        pane-care-southbank.com.au
      </li>
    </ul>
  </section>

  <section class="card card--back">
    <div class="brand">
      <span class="brand__name">GLEAM</span>
      <span class="brand__tagline">WINDOW CLEANING</span>
    </div>
    <p class="site">www.pane-care-southbank.com.au</p>
  </section>
</main>
</body>
</html>
```